Business Card - Business Consultancy

Newly Established Company, specializing in Business Consultancy, Human Resource Management, Talent Acquisition and Payroll Solutions.

We need a Business card design which portrays "elegance" and a very sleek yet business-like design. We would like a nice blue trimming (which goes well with the logo) to separate the content of the business card at the top. We would also like to see the design using the color silver either as a background or incorporated into it.

The final design should be a Business card which has colors matching the logo; a nice font; the above-mentioned specifics that adheres to the theme of "a stylish and professional business"

FYI: please do not have too fanciful designs.

Industry/Entity Type

Business Consultant

Contact Information for Business Card

Darren Loh
Business Development Director
Opal Staffing Advisory Private Limited
27 Marlow Street, #05-03B
Crescent Harbour Tower
Singapore 061732
Mobile : (+65) 93584617
Email : dloh@opalstaffing-advisory.com
Alternative : opalstaffingadvisory@mailvista.com

Requirements
Must have
• Nice Blue Trimming matching Logo which separates content, see attached
• Design incorporates either a silver background or the use of the color silver
Should not have
• No Fanciful Designs
• No Childish Designs
• No Overly Complicated Designs

```html
<!DOCTYPE html>
<html lang="en">
<head>
<meta charset="utf-8">
<title>Opal Staffing Advisory – Business Card</title>
<link href="https://fonts.googleapis.com/css2?family=Source+Sans+3:wght@400;600&display=swap" rel="stylesheet">
<style>
  :root {
    --backdrop: #3a3431;
    --card: #141414;
    --brand-blue: #1f8fd8;
    --brand-green: #8cc63f;
    --silver: #c0c0c0;
    --silver-dark: #8a8a8a;
    --ink: #f2f2f2;
  }
  * { box-sizing: border-box; margin: 0; padding: 0; }
  html, body {
    width: 1200px;
    height: 814px;
    overflow: hidden;
    background: var(--backdrop);
    font-family: "Source Sans 3", sans-serif;
  }
  .stage {
    position: relative;
    width: 1200px;
    height: 814px;
  }
  .card {
    position: absolute;
    top: 252px;
    width: 525px;
    height: 310px;
    background: var(--card);
    box-shadow: 0 10px 30px rgba(0,0,0,.45);
    overflow: hidden;
  }
  .card--contact { left: 50px; }
  .card--brand { left: 625px; }

  /* blue trimming with silver edge along the top */
  .trim {
    position: absolute;
    left: 0;
    right: 0;
    top: 0;
    height: 6px;
    background: var(--brand-blue);
    border-bottom: 2px solid var(--silver);
  }

  /* contact side */
  .mark-area {
    position: absolute;
    left: 28px;
    top: 80px;
    width: 150px;
    display: flex;
    flex-direction: column;
    align-items: center;
    gap: 12px;
  }
  .mark-area__name {
    color: var(--brand-blue);
    font-weight: 600;
    font-size: 18px;
  }
  .divider {
    position: absolute;
    left: 200px;
    top: 42px;
    width: 2px;
    height: 232px;
    background: linear-gradient(to bottom, var(--silver-dark), var(--silver), var(--silver-dark));
  }
  .details {
    position: absolute;
    left: 218px;
    top: 44px;
    color: var(--ink);
    font-size: 14.5px;
    line-height: 1.34;
    white-space: nowrap;
  }
  .details__name {
    color: var(--brand-blue);
    font-weight: 600;
    font-size: 19px;
    line-height: 1.1;
  }
  .details__title {
    color: var(--brand-green);
    font-size: 14.5px;
    margin-bottom: 6px;
  }
  .details__line { display: flex; align-items: center; gap: 8px; }
  .details__line svg { flex: none; }
  .details__alt { margin-top: 2px; font-size: 12.5px; }
  .details__alt span { text-decoration: underline; }

  /* brand side */
  .brand {
    position: absolute;
    left: 0;
    right: 0;
    top: 95px;
    display: flex;
    justify-content: center;
    align-items: center;
    gap: 14px;
  }
  .brand__name {
    color: var(--brand-blue);
    font-weight: 600;
    font-size: 34px;
    letter-spacing: .5px;
  }
  .web {
    position: absolute;
    left: 0;
    right: 0;
    bottom: 62px;
    text-align: center;
    color: var(--silver);
    font-size: 14px;
    letter-spacing: 1px;
  }
</style>
</head>
<body>
<main class="stage">
  <section class="card card--contact">
    <div class="trim"></div>
    <div class="mark-area">
      <svg width="110" height="110" viewBox="0 0 110 110" aria-hidden="true">
        <circle cx="55" cy="55" r="48" fill="none" stroke="var(--brand-blue)" stroke-width="8"/>
      </svg>
      <span class="mark-area__name">Opal Staffing</span>
    </div>
    <div class="divider"></div>
    <div class="details">
      <p class="details__name">Darren Loh</p>
      <p class="details__title">Business Development Director</p>
      <p>Opal Staffing Advisory Private Limited</p>
      <p>27 Marlow Street, #05-03B</p>
      <p>Crescent Harbour Tower</p>
      <p>Singapore 061732</p>
      <p class="details__line">
        <svg width="10" height="15" viewBox="0 0 10 15" aria-hidden="true"><rect x="1" y="1" width="8" height="13" rx="1.5" fill="none" stroke="var(--brand-blue)" stroke-width="1.5"/><circle cx="5" cy="11.5" r=".9" fill="var(--brand-blue)"/></svg>
        (+65) 93584617
      </p>
      <p class="details__line">
        <svg width="14" height="10" viewBox="0 0 14 10" aria-hidden="true"><rect width="14" height="10" fill="var(--brand-blue)"/><path d="M0 0 L7 6 L14 0" fill="none" stroke="var(--card)" stroke-width="1.3"/></svg>
        dloh@opalstaffing-advisory.com
      </p>
      <p class="details__alt">Alternative: <span>opalstaffingadvisory@mailvista.com</span></p>
    </div>
  </section>

  <section class="card card--brand">
    <div class="trim"></div>
    <div class="brand">
      <svg width="56" height="56" viewBox="0 0 56 56" aria-hidden="true">
        <circle cx="28" cy="28" r="24" fill="none" stroke="var(--brand-blue)" stroke-width="5"/>
      </svg>
      <span class="brand__name">Opal Staffing</span>
    </div>
    <p class="web">www.opalstaffing-advisory.com</p>
  </section>
</main>
</body>
</html>
```